Kelmor Builders usa, Inc

We need to create a flyer eg. 6"x11" or eg.9"x9" (looking for original format) in order to present our renovation company. www.kelmorbuilders.com for latest pictures please check www.kelmorbuilders.dwellpix.com

The idea is to send between 5000 to 10,000 flyers in our area Miami Beach and to present to potential clients our work in remodeling and interior renovation. We want to use the picture we have posted on www.kelmorbuilders.dwellpix.com (we have more new pictures coming soon)

We are trying to display at least 10 pictures on the flyer as well as our phone number/ name of the company. logo/ website address / a small text about the company and the space for the postage information.

Design has to be with modern lines

Voila…

Thanks

Brent
Updates

JULY 14, 2014 update. Please see the white flyer (dwellon) lets make its simple this is what we need to do. Adress will be 2716 harlow ave I surfside, fl I 33871 kelmorbuilders.com I (305) 555-0147

JULY 14, 2014 update. Adress will be 2716 harlow ave I surfside, fl I 33871 kelmorbuilders.com I (305) 555-0147

MUST HAVE THE POSTAL INFORMATION PLEASE SEE LAST TWO SCREEN SHOTS POSTED. POSTAGE INFORMATION SHOULD BE INSERT ON THE TOP RIGHT END CORNER SEE SCREEN SHOT FOR DETAILS THANKS

Target Market(s)

Home owners between 35 to 60 who have a renovation project in mind budget starting around $ 50 000 and up..

Industry/Entity Type

It Company

Font styles to use
Sans Serif

Requirements
Must have
• MUST HAVE THE POSTAL INFORMATION PLEASE SEE LAST TWO SCREEN SHOT POSTED. POSTAGE INFORMATION SHOULD BE INSERT ON THE TOP RIGHT END CORNER SEE SCREEN SHOT FOR DETAILS

THANKS

The flyer will just be double sided
we are working on a referral program so maybe we should leave a space too put one line for the referral program adress
Nice to have
• We like the colors on the picture green and brown (marco Desanti) or we can do a white flyer just giving some ides

```html
<!DOCTYPE html>
<html lang="en">
<head>
<meta charset="utf-8">
<title>Kelmor Builders – Flyer Front and Back</title>
<link rel="stylesheet" href="https://fonts.googleapis.com/css2?family=Archivo+Black&family=Cinzel:wght@900&family=Open+Sans:wght@400;600&display=swap">
<style>
  :root {
    --ink: #000;
    --brown-dark: #2a1a0e;
    --brown-mid: #4a3120;
    --brown-warm: #6b4a30;
    --cream: #efe4d2;
    --white: #ffffff;
    --label-grey: #8c8c8c;
    --banner-grey: #4a4a4a;
    --panel-grey: #3a3a3a;
    --panel-dark: #262626;
    --quote-ink: #22160c;
    --footer-band: #2a2614;
    --footer-text: #a89e86;
    --photo-edge: #f4f4f4;
    --card-fill: rgba(40,28,20,.78);
  }
  * { box-sizing: border-box; margin: 0; padding: 0; }
  html, body { width: 1200px; height: 1000px; overflow: hidden; background: var(--ink); }
  body { position: relative; font-family: "Open Sans", sans-serif; }

  /* ---------- FRONT FLYER ---------- */
  .flyer-front {
    position: absolute; left: 14px; top: 14px; width: 574px; height: 658px; overflow: hidden;
    background:
      repeating-linear-gradient(180deg, rgba(0,0,0,.28) 0 7px, transparent 7px 19px) top / 100% 70px no-repeat,
      radial-gradient(ellipse at 70% 40%, var(--brown-warm), var(--brown-mid) 45%, var(--brown-dark) 100%);
  }
  .flyer-front__band {
    position: absolute; left: 0; right: 0; top: 118px; height: 140px;
    background: linear-gradient(90deg, rgba(255,255,255,0) 40%, rgba(255,255,255,.12) 60%, rgba(255,255,255,.06));
  }
  .photo {
    position: absolute; border: 4px solid var(--photo-edge);
    box-shadow: 2px 3px 8px rgba(0,0,0,.6);
  }
  .photo--hall    { left: -2px;  top: 72px;  width: 136px; height: 142px; transform: rotate(2deg);  background: linear-gradient(160deg,#d8d4cc,#8f8a82); }
  .photo--living  { left: 128px; top: 60px;  width: 146px; height: 150px; transform: rotate(-2deg); background: linear-gradient(170deg,#d9d4cc,#6a5040); }
  .photo--garden  { left: -2px;  top: 222px; width: 130px; height: 145px; transform: rotate(-1deg); background: linear-gradient(180deg,#7a9cae,#5e8a4c); }
  .photo--stairs  { left: 134px; top: 218px; width: 150px; height: 148px; transform: rotate(2deg);  background: linear-gradient(150deg,#dcdcd8,#8a8784); }
  .photo--lounge  { left: -2px;  top: 372px; width: 142px; height: 146px; transform: rotate(2deg);  background: linear-gradient(175deg,#d2cdc4,#6a5444); }
  .photo--kitchen { left: 144px; top: 362px; width: 146px; height: 148px; transform: rotate(-2deg); background: linear-gradient(180deg,#c9a6b4,#8a3a5c); }
  .photo--ocean   { left: -2px;  top: 520px; width: 146px; height: 145px; transform: rotate(-2deg); background: linear-gradient(160deg,#7ab0c4,#3a4a52); }
  .photo--bedroom { left: 150px; top: 514px; width: 146px; height: 145px; transform: rotate(2deg);  background: linear-gradient(180deg,#9a8676,#d8d2c8); }
  .photo--plants  { left: 300px; top: 506px; width: 146px; height: 146px; transform: rotate(-2deg); background: linear-gradient(180deg,#d4d8da,#5a6458); }
  .photo--studio  { left: 450px; top: 498px; width: 126px; height: 146px; transform: rotate(3deg);  background: linear-gradient(170deg,#d0ccc6,#8a7d72); }

  .brand { position: absolute; left: 288px; top: 134px; color: var(--white); }
  .brand__name {
    font-family: "Open Sans", sans-serif; font-weight: 600; font-size: 36px;
    line-height: 1.02; letter-spacing: 1px;
  }
  .brand__tagline { margin-top: 10px; font-size: 12px; font-weight: 400; }

  .contact-card {
    position: absolute; left: 312px; top: 285px; width: 262px; height: 180px;
    background: rgba(255,255,255,.14); transform: rotate(-3deg); padding: 12px;
  }
  .contact-card__cta {
    background: var(--card-fill); height: 62px; color: var(--cream);
    text-align: center; padding-top: 9px; font-size: 15px; line-height: 1.35;
  }
  .contact-card__details {
    margin-top: 14px; background: var(--card-fill); height: 72px; color: var(--cream);
    padding: 12px 12px; font-size: 13px;
  }
  .contact-card__row { display: flex; align-items: center; gap: 8px; margin-bottom: 8px; }
  .contact-card__row svg { width: 15px; height: 15px; flex: none; }

  /* ---------- LABEL PANELS ---------- */
  .label-panel {
    position: absolute; overflow: hidden;
    background: radial-gradient(ellipse at 50% 45%, var(--panel-grey), var(--panel-dark));
  }
  .label-panel--back  { left: 602px; top: 0;     width: 598px; height: 313px; }
  .label-panel--front { left: 0;     top: 687px; width: 600px; height: 313px; }
  .label-panel svg { position: absolute; left: 0; top: 0; }
  .label-panel__word {
    position: absolute; font-family: "Archivo Black", sans-serif; color: var(--label-grey);
    font-size: 150px; line-height: 1;
  }
  .label-panel--back .label-panel__word  { left: 52px; top: 34px; letter-spacing: 6px; }
  .label-panel--front .label-panel__word { left: 22px; top: 158px; letter-spacing: 2px; }

  /* ---------- BACK FLYER ---------- */
  .flyer-back {
    position: absolute; left: 614px; top: 326px; width: 574px; height: 660px; overflow: hidden;
    background: radial-gradient(ellipse at 50% 30%, #5e4330, #3e2a1b 50%, #2a1c11 100%);
    color: var(--cream); text-align: center;
  }
  .postage-indicia {
    position: absolute; right: 12px; top: 8px; width: 92px; height: 42px;
    border: 1px solid rgba(239,228,210,.55); color: rgba(239,228,210,.8);
    font-size: 8px; line-height: 12px; padding-top: 2px; letter-spacing: .3px;
  }
  .about {
    position: absolute; left: 46px; right: 46px; top: 56px;
    font-size: 13.6px; line-height: 18.6px;
  }
  .about p + p { margin-top: 18px; }
  .projects-band {
    position: absolute; left: 0; right: 0; top: 320px; height: 54px;
    background: linear-gradient(90deg, transparent, rgba(0,0,0,.35) 20%, rgba(0,0,0,.35) 80%, transparent);
    font-size: 13px; line-height: 17px; padding-top: 8px;
  }
  .quote {
    position: absolute; left: 0; right: 0; top: 400px;
    font-family: "Cinzel", serif; font-weight: 900; color: var(--quote-ink);
    font-variant: small-caps; font-size: 38px; line-height: 48px; letter-spacing: 2px;
    text-shadow: 0 1px 0 rgba(255,255,255,.08);
  }
  .quote__author {
    position: absolute; left: 288px; top: 538px;
    font-family: "Cinzel", serif; font-weight: 900; font-variant: small-caps;
    color: var(--quote-ink); font-size: 22px; letter-spacing: 1px;
  }
  .address-band {
    position: absolute; left: 0; right: 0; bottom: 0; height: 66px;
    background: var(--footer-band); border-top: 1px solid rgba(255,255,255,.08);
    font-size: 11.5px; color: var(--footer-text); text-align: left; padding: 24px 0 0 96px;
  }
  .address-band span + span { margin-left: 42px; }
</style>
</head>
<body>

  <section class="flyer-front">
    <div class="flyer-front__band"></div>
    <div class="photo photo--hall"    role="img" aria-label="Project photo: glass-walled hallway"></div>
    <div class="photo photo--living"  role="img" aria-label="Project photo: living room"></div>
    <div class="photo photo--garden"  role="img" aria-label="Project photo: villa garden and pool"></div>
    <div class="photo photo--stairs"  role="img" aria-label="Project photo: staircase"></div>
    <div class="photo photo--lounge"  role="img" aria-label="Project photo: lounge"></div>
    <div class="photo photo--kitchen" role="img" aria-label="Project photo: kitchen"></div>
    <div class="photo photo--ocean"   role="img" aria-label="Project photo: ocean view from balcony"></div>
    <div class="photo photo--bedroom" role="img" aria-label="Project photo: bedroom"></div>
    <div class="photo photo--plants"  role="img" aria-label="Project photo: terrace planters"></div>
    <div class="photo photo--studio"  role="img" aria-label="Project photo: room with artwork"></div>

    <div class="brand">
      <div class="brand__name">KELMOR<br>BUILDERS</div>
      <div class="brand__tagline">Construction &nbsp;|&nbsp; Management &nbsp;|&nbsp; Design Studio</div>
    </div>

    <div class="contact-card">
      <div class="contact-card__cta">Renovation in mind?<br>Contact Us!</div>
      <div class="contact-card__details">
        <div class="contact-card__row">
          <svg viewBox="0 0 16 16" fill="none" stroke="currentColor" stroke-width="1.3"><circle cx="8" cy="8" r="6.5"/><ellipse cx="8" cy="8" rx="2.8" ry="6.5"/><path d="M1.5 8h13M2.5 4.8h11M2.5 11.2h11"/></svg>
          <span>www.kelmorbuilders.com</span>
        </div>
        <div class="contact-card__row">
          <svg viewBox="0 0 16 16" fill="currentColor"><path d="M3.6 1.5l2.3 2.6-1.3 1.8c.9 2 2.4 3.6 4.4 4.5l1.8-1.3 2.7 2.2-1.2 2.6C7 13.6 2.4 9 1.2 3z"/></svg>
          <span>(305) 555-0193</span>
        </div>
      </div>
    </div>
  </section>

  <div class="label-panel label-panel--back">
    <svg width="598" height="313" viewBox="0 0 598 313"><polygon points="55,160 543,160 543,220 299,281 55,220" fill="var(--banner-grey)"/></svg>
    <div class="label-panel__word">BACK</div>
  </div>

  <div class="label-panel label-panel--front">
    <svg width="600" height="313" viewBox="0 0 600 313"><polygon points="24,82 300,23 580,82 580,168 24,168" fill="var(--banner-grey)"/></svg>
    <div class="label-panel__word">FRONT</div>
  </div>

  <section class="flyer-back">
    <div class="postage-indicia">PRSRT STD<br>U.S. POSTAGE PAID<br>PERMIT NO. 000</div>
    <div class="about">
      <p>Kelmor Builders, inc is a construction management group, headquartered in Miami beach provides construction management, general contracting services as well as interior design palette packages to a respected client-base. Founded on the principles of trust, team work and loyalty, Kelmor Builders, Inc delivers the highest quality products and services.</p>
      <p>After 10 years of teamwork, Kelmor Builders has become a cohesive, respected team of professionals specializing in residential and commercial construction and renovation for small to mid-sized projects. Always striving for perfection, we pride ourselves on our reputation for trustworthiness, professionalism and efficiency. Kelmor Builders turn interior renovation projects into reality and that is our everyday goal.</p>
    </div>
    <div class="projects-band">Projects<br>starting from $50,000</div>
    <div class="quote">“Every act of creation<br>is first<br>an act of destruction.”</div>
    <div class="quote__author">-Aurelio Vance</div>
    <div class="address-band"><span>Physical Address:</span><span>2716 Harlow Avenue # 806, Surfside, FL 33871</span></div>
  </section>

</body>
</html>
```